Stationery Design Project

KT7 Staffing requires letterhead and business card designs for a company based in London. Just like the name, we're a management resourcing company, providing resources to third party companies. You can see www.kt7staffing-example.com for ideas on existing colour schemes and design concepts that have been implimented and agreed to. Ultimately the design should broadcast professionalism, safety and the concept of growth.

Target Market(s)

Financial institutes; friendly societies (All UK based)

Industry/Entity Type

Safety

Requirements
Must have
• Files produced should be print ready; and the text in them editable (eg address, name etc)

```html
<!DOCTYPE html>
<html lang="en">
<head>
<meta charset="utf-8">
<title>KT7 Staffing Letterhead</title>
<link href="https://fonts.googleapis.com/css2?family=Arimo:wght@400;700&display=swap" rel="stylesheet">
<style>
  :root {
    --teal: #1a9fae;
    --teal-text: #16939f;
    --sky: #72bfdd;
    --sky-text: #7cc3dc;
    --paper: #ffffff;
    --backdrop: #ffffff;
  }
  html, body {
    margin: 0;
    width: 1200px;
    height: 900px;
    overflow: hidden;
    background: var(--backdrop);
    font-family: "Arimo", Arial, sans-serif;
  }
  .canvas { position: relative; width: 1200px; height: 900px; }
  .letterhead {
    position: absolute;
    left: 304px; top: 30px;
    width: 594px; height: 840px;
    background: var(--paper);
    border: 1px solid #d6d6d6;
    box-shadow: 3px 4px 5px rgba(0,0,0,0.45);
    overflow: hidden;
  }
  .brand {
    position: absolute;
    left: 18px; top: 26px;
    display: flex; align-items: center; gap: 12px;
  }
  .brand-mark {
    width: 30px; height: 30px;
    background: var(--sky);
  }
  .brand-name {
    font-size: 30px;
    font-weight: 700;
    color: var(--teal-text);
    letter-spacing: -0.5px;
    line-height: 1;
  }
  .divider {
    position: absolute;
    top: 25px; width: 1px; height: 50px;
    background: var(--sky);
  }
  .divider--address { left: 287px; }
  .divider--contact { left: 448px; }
  .details {
    position: absolute; top: 29px;
    display: grid; column-gap: 6px; row-gap: 0;
    font-size: 8px; line-height: 12px;
  }
  .details dt { font-weight: 700; color: var(--teal-text); text-align: right; }
  .details dd { margin: 0; color: var(--sky-text); }
  .details--address { left: 299px; grid-template-columns: auto auto; }
  .details--contact { left: 459px; grid-template-columns: 27px auto; }
  .footer {
    position: absolute; left: 0; bottom: 0;
    width: 594px; height: 52px;
  }
  .footer svg { position: absolute; inset: 0; }
  .footer-url {
    position: absolute; left: 0; right: 0; bottom: 12px;
    text-align: center;
    color: #ffffff;
    font-size: 10px; font-weight: 700;
  }
</style>
</head>
<body>
<div class="canvas">
  <section class="letterhead">
    <header>
      <div class="brand">
        <span class="brand-mark"></span>
        <span class="brand-name">KT7 STAFFING</span>
      </div>
      <span class="divider divider--address"></span>
      <dl class="details details--address">
        <dt>Address</dt><dd>Harlow Mews Rd</dd>
        <dt></dt><dd>Kingsmere Park</dd>
        <dt></dt><dd>London SE9 4QT England</dd>
      </dl>
      <span class="divider divider--contact"></span>
      <dl class="details details--contact">
        <dt>Phone</dt><dd>+44 20 55 010203</dd>
        <dt>Fax</dt><dd>+44 20 55 010204</dd>
        <dt>Email</dt><dd>info@kt7staffing-example.com</dd>
      </dl>
    </header>
    <footer class="footer">
      <svg viewBox="0 0 594 52" width="594" height="52" preserveAspectRatio="none">
        <path d="M0 16 Q297 -8 594 16 L594 52 L0 52 Z" fill="var(--sky)"/>
        <path d="M0 28 Q297 8 594 28 L594 52 L0 52 Z" fill="var(--teal)"/>
      </svg>
      <div class="footer-url">www.kt7staffing-example.com</div>
    </footer>
  </section>
</div>
</body>
</html>
```